Label for Wines Design

I need a label design for a start-up business that makes grape wines. The label of wine features a picture frame on the edges of the wine bottle label. So each style of wine (red, white, sparkling, rose etc) will feature a different colour. As you can picture there is already a lot going on in this label.

My trademark is 'tumo', means 'Virgin pure love',type of wines: Sauvignon Blanc, Merlot, Pino noir etc. All in Caps, a Juxtaposition of old & modern. Bold & thick letters to grab attention on the wine store shelves. Maybe letter spacing squeezed together as the wine label is only 4inches wide...the text 'tumo' must fit on one line! No Cursive or curvy lines! Colors open to black, green, yellow, purple must be natural colors hues in nature.

New Zealand wines are New worlds wines,green and astringency,unique fruity, just as virgin pure love, is an infatuation, lovesickness, never forget......

Target Market(s)

New Zealand and Asian
food & wine lovers all ages

Industry/Entity Type

Business

Font styles to use
Decorative
Script

Colors

Designer to choose colors to be used in the design.

Requirements
Must have
• Front Label and back label
Nice to have
• Wines-feeling is green and astringency,unique fruity, just as virgin pure love, is an infatuation, lovesickness, never forget......

```html
<!DOCTYPE html>
<html lang="en">
<head>
<meta charset="utf-8">
<title>tumo wine labels</title>
<link href="https://fonts.googleapis.com/css2?family=Cinzel:wght@400;600;700&family=Arimo&family=Tinos&display=swap" rel="stylesheet">
<style>
  :root {
    --canvas: #ffffff;
    --paper: #ffffff;
    --ink: #111111;
    --ink-soft: #6b6b6b;
    --merlot-light: #a40f0f;
    --merlot-mid: #6e0d12;
    --merlot-dark: #2a0506;
    --blanc-light: #dcec4a;
    --blanc-mid: #b9dc1c;
    --blanc-dark: #8bbd0b;
  }
  * { margin: 0; padding: 0; box-sizing: border-box; }
  html, body { width: 1200px; height: 800px; overflow: hidden; background: var(--canvas); }
  .canvas { position: relative; width: 1200px; height: 800px; }

  .label {
    position: absolute;
    top: 105px;
    width: 250px;
    height: 585px;
    background: var(--paper);
    box-shadow: 0 0 8px rgba(0,0,0,0.35);
  }
  .label--merlot { left: 237px; }
  .label--blanc { left: 703px; }

  .vintage {
    position: absolute; top: 36px; left: 0; width: 100%;
    text-align: center;
    font-family: "Cinzel", serif; font-weight: 700; font-size: 22px;
    letter-spacing: 1px; color: var(--ink);
  }

  .seal {
    position: absolute; left: -55px; top: 80px;
    width: 360px; height: 360px;
  }

  .brand {
    position: absolute; top: 184px; left: -30px; width: 320px;
    text-align: center;
    font-family: "Cinzel", serif; font-weight: 400; font-size: 70px;
    line-height: 1; letter-spacing: -2px; color: var(--ink);
  }
  .tagline {
    position: absolute; top: 268px; left: -30px; width: 320px;
    text-align: center;
    font-family: "Arimo", sans-serif; font-size: 19px;
    letter-spacing: 0.3px; color: var(--ink-soft);
  }
  .varietal {
    position: absolute; top: 330px; left: -30px; width: 320px;
    text-align: center;
    font-family: "Cinzel", serif; font-weight: 600; font-size: 20px;
    color: var(--ink);
  }
  .label--merlot .varietal { font-size: 26px; top: 327px; }

  .origin {
    position: absolute; top: 459px; left: 0; width: 100%;
    text-align: center;
    font-family: "Tinos", serif; font-size: 12px; line-height: 17px;
    color: var(--ink);
  }

  .specs {
    position: absolute; bottom: 10px; left: 8px; right: 10px;
    display: flex; justify-content: space-between;
    font-family: "Cinzel", serif; font-weight: 700; font-size: 20px;
    color: var(--ink);
  }
</style>
</head>
<body>
<main class="canvas">

  <section class="label label--merlot">
    <p class="vintage">2017</p>
    <svg class="seal" viewBox="0 0 360 360" aria-hidden="true">
      <defs>
        <linearGradient id="merlot-ring" x1="0" y1="0" x2="1" y2="0">
          <stop offset="0" style="stop-color: var(--merlot-light)"/>
          <stop offset="0.45" style="stop-color: var(--merlot-mid)"/>
          <stop offset="1" style="stop-color: var(--merlot-dark)"/>
        </linearGradient>
        <filter id="merlot-shadow" x="-10%" y="-10%" width="120%" height="120%">
          <feDropShadow dx="0" dy="0" stdDeviation="3" flood-opacity="0.4"/>
        </filter>
      </defs>
      <circle cx="180" cy="180" r="174" fill="#fff" filter="url(#merlot-shadow)"/>
      <path fill="url(#merlot-ring)" fill-rule="evenodd"
            d="M180 10 a170 170 0 1 0 0.01 0 Z M188 35 a145 145 0 1 0 0.01 0 Z"/>
    </svg>
    <h1 class="brand">TUMO</h1>
    <p class="tagline">NEW WORLDS WINES</p>
    <h2 class="varietal">MERLOT</h2>
    <p class="origin">NEW ZEALAND<br>FRENCH WINES</p>
    <div class="specs"><span>13,3% Vol</span><span>75cle</span></div>
  </section>

  <section class="label label--blanc">
    <p class="vintage">2017</p>
    <svg class="seal" viewBox="0 0 360 360" aria-hidden="true">
      <defs>
        <linearGradient id="blanc-ring" x1="0" y1="0" x2="1" y2="0">
          <stop offset="0" style="stop-color: var(--blanc-light)"/>
          <stop offset="0.5" style="stop-color: var(--blanc-mid)"/>
          <stop offset="1" style="stop-color: var(--blanc-dark)"/>
        </linearGradient>
        <filter id="blanc-shadow" x="-10%" y="-10%" width="120%" height="120%">
          <feDropShadow dx="0" dy="0" stdDeviation="3" flood-opacity="0.4"/>
        </filter>
      </defs>
      <circle cx="180" cy="180" r="174" fill="#fff" filter="url(#blanc-shadow)"/>
      <path fill="url(#blanc-ring)" fill-rule="evenodd"
            d="M180 10 a170 170 0 1 0 0.01 0 Z M188 35 a145 145 0 1 0 0.01 0 Z"/>
    </svg>
    <h1 class="brand">TUMO</h1>
    <p class="tagline">NEW WORLDS WINES</p>
    <h2 class="varietal">SAUVIGNON BLANC</h2>
    <p class="origin">NEW ZEALAND<br>FRENCH WINES</p>
    <div class="specs"><span>13,3% Vol</span><span>75cle</span></div>
  </section>

</main>
</body>
</html>
```